Coastal Sentinels Stationery Design Project

I am looking for a suitable stationary design for my company Coastal Sentinels Pty Ltd (ACN 508 214 396).

The requirements can be better explained by visiting my website
"coastal-sentinels.org"

I will be sending letters to Ministers of State and the Heads of Government Agencies so the theme needs to be formal and serious.

A theme with a shield or similar picking on the "guardian" concept would be appropriate

Target Market(s)

Ministers of State and Department Agency Heads and legal firms, the heads of Trustee Companies as well as Members of Coastal Sentinels

Industry/Entity Type

Government

Requirements
Must have
• Letterhead design is a priority - Business Card secondary

Must include tag line "Shielding your savings when the rest walk away" with a registered trade mark superscript at the end that is an R in a circle {Windows Alt +0174 on numeric keypad or Mac Option +R}.

Must include website address "Coastal-Sentinels.org" plus Email address "coastsentinel@fernmail.net

Company name "Coastal Sentinels Pty. Ltd." and Australian Company Number "ACN 508 214 396" needs to be shown more discretely

Address is "47 Brookfern Lane, Marlow Vale, 3281"
Nice to have
• A watermark is something to be considered

```html
<!DOCTYPE html>
<html lang="en">
<head>
<meta charset="utf-8">
<title>Coastal Sentinels Stationery</title>
<link href="https://fonts.googleapis.com/css2?family=Barlow:wght@400;500;600&display=swap" rel="stylesheet">
<style>
  :root {
    --backdrop: #d4d4d4;
    --paper: #fcfbf0;
    --plum: #4f2148;
    --plum-soft: #5e2e57;
    --slate: #8b8b8b;
    --watermark: #efeee4;
    --font: "Barlow", Arial, sans-serif;
  }
  * { box-sizing: border-box; margin: 0; padding: 0; }
  html, body { width: 1200px; height: 900px; overflow: hidden; }
  body { background: var(--backdrop); font-family: var(--font); position: relative; }

  .letterhead {
    position: absolute; left: 150px; top: 40px; width: 590px; height: 820px;
    background: var(--paper);
  }
  .brand { position: absolute; display: flex; align-items: center; gap: 10px; }
  .brand-mark { background: var(--plum); flex: none; }
  .brand-name { color: var(--plum); font-weight: 600; line-height: 1; white-space: nowrap; }
  .brand-tagline { color: var(--slate); font-weight: 500; line-height: 1.1; white-space: nowrap; }
  .brand-tagline sup { font-size: 0.6em; }

  .letterhead .brand { left: 36px; top: 52px; }
  .letterhead .brand-mark { width: 44px; height: 44px; }
  .letterhead .brand-name { font-size: 28px; }
  .letterhead .brand-tagline { font-size: 13.5px; margin-top: 2px; }

  .letterhead-contact {
    position: absolute; right: 28px; top: 52px; text-align: right;
    color: var(--plum); font-size: 11px; font-weight: 600; line-height: 1.45;
  }
  .watermark {
    position: absolute; left: 185px; top: 270px; width: 220px; height: 220px;
    background: var(--watermark);
  }
  .letterhead-legal {
    position: absolute; right: 26px; bottom: 36px; text-align: right;
    color: var(--slate); font-size: 11px; font-weight: 600; line-height: 1.35;
  }

  .card { position: absolute; left: 790px; width: 290px; height: 168px; }
  .card-front { top: 368px; background: var(--paper); }
  .card-back { top: 556px; background: var(--plum); overflow: hidden; }

  .card-front .brand { left: 20px; top: 14px; gap: 6px; }
  .card-front .brand-mark { width: 26px; height: 26px; }
  .card-front .brand-name { font-size: 15px; }
  .card-front .brand-tagline { font-size: 7.5px; }
  .card-person { position: absolute; left: 24px; top: 60px; color: var(--plum); }
  .card-person-name { font-size: 10px; font-weight: 600; }
  .card-person-role { font-size: 7px; color: var(--slate); }
  .card-details {
    position: absolute; left: 24px; top: 94px; font-size: 7.5px; line-height: 1.4;
    color: var(--plum); font-weight: 600;
  }
  .card-details span { color: var(--slate); font-weight: 500; }

  .card-back-panel {
    position: absolute; right: 22px; top: 10px; width: 130px; height: 150px;
    background: var(--plum-soft);
  }
  .card-back .brand { left: 50px; top: 62px; gap: 6px; }
  .card-back .brand-mark { width: 26px; height: 26px; background: #ffffff; }
  .card-back .brand-name { color: #ffffff; font-size: 15px; }
  .card-back .brand-tagline { color: #d9c9d5; font-size: 7.5px; }
  .card-back-web {
    position: absolute; left: 0; right: 0; bottom: 22px; text-align: center;
    color: #ffffff; font-size: 8px; font-weight: 600;
  }
</style>
</head>
<body>
  <section class="letterhead">
    <div class="brand">
      <div class="brand-mark"></div>
      <div>
        <div class="brand-name">Coastal Sentinels</div>
        <div class="brand-tagline">Shielding your savings when the rest walk away<sup>®</sup></div>
      </div>
    </div>
    <address class="letterhead-contact" style="font-style:normal">
      47 Brookfern Lane,<br>Marlow Vale, 3281<br>coastsentinel@fernmail.net<br>www.Coastal-Sentinels.org
    </address>
    <div class="watermark" role="img" aria-label="Faint watermark shape"></div>
    <div class="letterhead-legal">Coastal Sentinels Pty Ltd<br>ACN 508 214 396</div>
  </section>

  <section class="card card-front">
    <div class="brand">
      <div class="brand-mark"></div>
      <div>
        <div class="brand-name">Coastal Sentinels</div>
        <div class="brand-tagline">Shielding your savings when the rest walk away<sup>®</sup></div>
      </div>
    </div>
    <div class="card-person">
      <div class="card-person-name">Hanna Treloar</div>
      <div class="card-person-role">Director</div>
    </div>
    <div class="card-details">
      47 Brookfern Lane,<br>Marlow Vale, 3281<br>
      <span>Phone:</span>0438 552 907<br>
      <span>Fax:</span> (03) 5521 8470<br>
      <span>Email:</span>coastsentinel@fernmail.net
    </div>
  </section>

  <section class="card card-back">
    <div class="card-back-panel"></div>
    <div class="brand">
      <div class="brand-mark"></div>
      <div>
        <div class="brand-name">Coastal Sentinels</div>
        <div class="brand-tagline">Shielding your savings when the rest walk away<sup>®</sup></div>
      </div>
    </div>
    <div class="card-back-web">www.Coastal-Sentinels.org</div>
  </section>
</body>
</html>
```